BQN - New Homepage needed for an existing website

Lantern of Meridel Website
Need a new Homepage for an existing website with Action Items and Newer Pictures
This is the current Website
https://lanternofmeridel.example/

This new page will be changed on Jan 21st when Voting begins
1. Voting like a political campaign where we are trying to raise awareness for the issues we stand for and urge the people to go to a Polling /voting website and vote for us (Roster 27)
2. We have 6 basic themes as to what we stand for - there will be text to promote their importance of voting/call to action
3. There will be videos on the website and there will be a simulation of how the voting process works - will be added later

Use colors like the US Flag - Red, White and Blue. The other pages don't need to be changed - only the HomePage.

I only need the design, I will code the website. Thank you

Target Market(s)

Jewish People in the US

Industry/Entity Type

Religious

Number of Pages Required

1 page

Font styles to use
Serif
Sans Serif

Colors

Designer to choose colors to be used in the design.

Requirements
Must have
• Call to Action - Go out to Vote
• This is the current Website - https://lanternofmeridel.example/

```html
<!DOCTYPE html>
<html lang="en">
<head>
<meta charset="utf-8">
<title>Lantern of Meridel – Homepage</title>
<link rel="stylesheet" href="https://fonts.googleapis.com/css2?family=Poppins:wght@300;400;500;600;700&display=swap">
<style>
:root{
  --navy:#0c2a55;
  --red:#9b0b0b;
  --red-bright:#b3121a;
  --ink:#333333;
  --muted:#7a7a7a;
  --light:#ececec;
  --white:#ffffff;
  --black:#050505;
}
*{box-sizing:border-box;margin:0;padding:0}
html,body{width:1200px;height:5054px;overflow:hidden}
body{font-family:"Poppins",sans-serif;color:var(--ink);background:var(--white);position:relative}
section,header,footer{position:absolute;left:0;width:1200px;overflow:hidden}
.pill{position:absolute;display:flex;align-items:center;justify-content:center;border-radius:30px;font-size:14px;font-weight:400}
.pill-outline{border:2px solid var(--white);color:var(--white)}
.pill-red{background:var(--red);color:var(--white)}
.pill-white{background:var(--white);color:var(--ink)}
.photo{position:absolute}

/* hero */
.hero{top:0;height:690px}
.hero .photo{inset:0;background:linear-gradient(110deg,#1d3b6b 0%,#4a2a55 45%,#8f1a22 75%,#a5121a 100%)}
.nav-brand{position:absolute;left:120px;top:36px;color:var(--white);font-weight:700;font-size:26px;letter-spacing:2px;display:flex;align-items:center;gap:10px}
.nav-brand .dot{width:16px;height:16px;border-radius:50%;background:var(--white)}
.nav-links{position:absolute;right:118px;top:38px;display:flex;align-items:center;gap:28px;color:var(--white);font-size:14px}
.nav-links .vote{border:2px solid var(--white);border-radius:26px;padding:12px 38px}
.hero-copy{position:absolute;top:258px;width:100%;text-align:center;color:var(--white)}
.hero-copy .kicker{font-size:24px;font-weight:400}
.hero-copy h1{font-size:60px;font-weight:700;letter-spacing:1px;line-height:1.2}
.hero-copy p{font-size:25px;font-weight:400;letter-spacing:1px}

/* bands */
.band h2{position:absolute;color:var(--white);font-size:50px;font-weight:700;line-height:58px;letter-spacing:1px}
.join{top:690px;height:236px;background:var(--navy)}
.continuity-band{top:2471px;height:237px;background:var(--red)}

/* video */
.videos{top:926px;height:478px;background:var(--black)}
.play{position:absolute;width:38px;height:38px}

/* points */
.points{top:1404px;height:1067px;background:var(--light)}
.points h2{position:absolute;top:96px;width:100%;text-align:center;font-size:52px;font-weight:700;line-height:72px;letter-spacing:1px;color:var(--ink)}
.diagram-area{position:absolute;left:380px;top:360px;width:460px;height:510px;border-radius:50%;background:radial-gradient(ellipse at center,#f6f6f6 0%,#e2e4ea 55%,rgba(236,236,236,0) 75%)}
.point{position:absolute;font-size:25px;color:#444;line-height:31px;letter-spacing:1px;text-align:center}
.point-core{font-weight:700;font-size:30px;line-height:38px;color:var(--ink)}

/* objectives */
.objectives{top:2708px;height:1033px;background:var(--white)}
.objectives h2{position:absolute;top:92px;width:100%;text-align:center;font-size:52px;font-weight:700;letter-spacing:1px}
.objective{position:absolute;width:290px;text-align:center}
.objective h3{font-size:16px;font-weight:500;line-height:22px;color:#222}
.objective p{margin-top:18px;font-size:11.5px;line-height:21px;color:var(--muted);font-weight:300}
.objective .pill{position:relative;margin:38px auto 0;width:186px;height:46px}

/* mission */
.mission{top:3741px;height:567px;background:#efefef}
.mission .photo{left:720px;top:0;width:480px;height:567px;background:linear-gradient(160deg,#d6d6d6 0%,#a8a8a8 45%,#6f6f6f 100%)}
.mission-copy{position:absolute;left:120px;top:86px;width:570px}
.mission-copy h2{font-size:50px;font-weight:700;letter-spacing:1px;color:var(--ink)}
.mission-copy h3{margin-top:22px;color:var(--red-bright);font-size:24px;font-weight:500;letter-spacing:1px}
.mission-copy p{margin-top:18px;font-size:11.5px;line-height:21px;color:var(--muted)}

/* quote */
.quote{top:4308px;height:330px}
.quote .photo{inset:0;background:linear-gradient(90deg,#173461 0%,#0f2b57 60%,#2c4470 100%)}
.quote .rule{position:absolute;left:567px;top:80px;width:66px;height:2px;background:var(--red-bright)}
.quote blockquote{position:absolute;top:118px;width:100%;text-align:center;color:var(--white);font-size:30px;font-weight:600;line-height:42px;letter-spacing:1px}

/* footer */
.site-footer{top:4638px;height:416px;background:var(--white)}
.divider{position:absolute;top:70px;width:1px;height:310px;background:#cfcfcf}
.footer-col h4{position:absolute;font-size:20px;font-weight:500;letter-spacing:1px;color:#222}
.quick-links{position:absolute;right:852px;top:120px;text-align:right;font-size:11.5px;line-height:28px;color:var(--muted)}
.contact-form{position:absolute;left:470px;top:115px;width:250px}
.contact-form .field{height:40px;border:1px solid #bdbdbd;border-radius:20px;margin-bottom:13px;padding:0 18px;display:flex;align-items:center;font-size:11px;color:#b5b5b5}
.contact-form .submit{height:40px;border-radius:20px;background:var(--red);color:var(--white);display:flex;align-items:center;justify-content:center;font-size:12px}
.about{position:absolute;left:838px;top:120px;width:250px;font-size:11.5px;line-height:26px;color:var(--muted)}
.socials{display:flex;gap:8px;margin-top:26px}
.socials span{width:28px;height:28px;border-radius:50%;background:#222}
.copyright{margin-top:36px}
</style>
</head>
<body>

<header class="hero">
  <div class="photo" role="img" aria-label="Photo of smiling young members of the Jewish community under a blue-to-red overlay"></div>
  <div class="nav-brand"><span class="dot"></span>BQN</div>
  <nav class="nav-links">
    <span>Home</span>
    <span>Lantern of Meridel ▾</span>
    <span class="vote">Vote Now</span>
  </nav>
  <div class="hero-copy">
    <div class="kicker">It’s All About</div>
    <h1>Jewish Community</h1>
    <p>We Embrace Our Past To Ensure Our Future</p>
  </div>
  <span class="pill pill-red" style="left:255px;top:456px;width:340px;height:46px">New Laws Increase Hate Crimes</span>
  <span class="pill pill-white" style="left:606px;top:456px;width:340px;height:46px">Join The Jewish Future</span>
</header>

<section class="band join">
  <h2 style="left:255px;top:60px">Join The Jewish<br>Future</h2>
  <span class="pill pill-outline" style="left:793px;top:94px;width:148px;height:46px">Vote Now</span>
</section>

<section class="videos">
  <div class="photo" style="left:137px;top:164px;width:203px;height:145px;background:linear-gradient(135deg,#6b3a1f,#b07a3c)" role="img" aria-label="Video thumbnail of a synagogue interior"></div>
  <div class="photo" style="left:375px;top:72px;width:450px;height:325px;background:linear-gradient(180deg,#d9d3c7 0%,#8a8a8a 45%,#3c3c3c 100%)" role="img" aria-label="Featured video player showing a crowd with umbrellas at a memorial"></div>
  <div class="photo" style="left:860px;top:160px;width:218px;height:148px;background:linear-gradient(135deg,#1e2a3a,#6b7080)" role="img" aria-label="Video thumbnail of a speaker"></div>
  <svg class="play" style="left:210px;top:218px" viewBox="0 0 38 38"><circle cx="19" cy="19" r="18" fill="#fff"/><path d="M15 11 L27 19 L15 27Z" fill="#222"/></svg>
  <svg class="play" style="left:950px;top:216px" viewBox="0 0 38 38"><circle cx="19" cy="19" r="18" fill="#fff"/><path d="M15 11 L27 19 L15 27Z" fill="#222"/></svg>
</section>

<section class="points">
  <h2>6 Points. 5 Minutes<br>1 New Bold Movement</h2>
  <div class="diagram-area" role="img" aria-label="Red and blue six-pointed star diagram linking the six points around Jewish Continuity"></div>
  <div class="point" style="left:460px;top:312px;width:300px">Jewish Pride</div>
  <div class="point" style="left:170px;top:462px;width:240px">Growing<br>Anti-Semitism</div>
  <div class="point" style="left:840px;top:470px;width:180px">Assimilation</div>
  <div class="point point-core" style="left:460px;top:560px;width:300px">Jewish<br>Continuity</div>
  <div class="point" style="left:185px;top:742px;width:200px">Israel In The<br>Jewish<br>Homeland</div>
  <div class="point" style="left:820px;top:738px;width:120px">BDS</div>
  <div class="point" style="left:400px;top:874px;width:420px">Israel Must Retain Its<br>True Traditional<br>Jewish Identity</div>
</section>

<section class="band continuity-band">
  <h2 style="left:240px;top:60px">It’s All About<br>Jewish Continuity</h2>
  <span class="pill pill-white" style="left:810px;top:96px;width:148px;height:46px">Vote Now</span>
</section>

<section class="objectives">
  <h2>Objectives</h2>
  <article class="objective" style="left:113px;top:228px">
    <h3>Confort<br>Anti-Semitism</h3>
    <p>Anti-Semitism In America Is Unfortunately, Becoming The New Norm. While The Attacks Against Jews In Pittsburgh And California Garnered A Lot Of Media Attention, There Are Ever-Increasing Incidents Of Hate Crimes Against The Jewish People In The U.S.</p>
    <span class="pill pill-red">Discover More</span>
  </article>
  <article class="objective" style="left:455px;top:228px">
    <h3>Resist<br>Assimilation</h3>
    <p>Assimilation Is An Issue Facing Every Religion. With Respect To Judaism, Lantern of Meridel Underscores The Need For Education Regarding Our History, Heritage And The Beauty Of Judaism.</p>
    <span class="pill pill-red" style="margin-top:34px">Discover More</span>
  </article>
  <article class="objective" style="left:787px;top:228px">
    <h3>Expose BDS</h3>
    <p style="margin-top:38px">BDS Has Not Yet Gained Enough Traction To Be A Real Threat Currently, But The Threat Of BDS Looms Large When Considering The Left-Leaning American College Environment. In Twenty Years, Today’s College Students Who Are Being Inculcated By BDS Will Inevitably Rise In Local Politics, Congress, Or Even National Office.</p>
    <span class="pill pill-red">Discover More</span>
  </article>
  <article class="objective" style="left:109px;top:612px">
    <h3>Instill Jewish<br>Pride</h3>
    <p>Due To The Atmosphere On Many If Not Most Of Our American College Campuses, Students Are Ashamed Or Scared To State That They Are Jewish, Or That They Support Israel. We Must Be Allowed To Stand Tall And Proud On College Campuses When We Identify As Jews And Support Israel.</p>
    <span class="pill pill-red">Discover More</span>
  </article>
  <article class="objective" style="left:455px;top:612px">
    <h3>Israel: The Eternal Jewish<br>Homeland</h3>
    <p>For Thousands Of Years, Judaism Has Been Inextricably Bound With Israel. Since 1948, Israel Has Been A Jewish State Based On Its Original Deed – The Torah That Was Given To Us At Mount Sinai, As Well As Worldwide Recognition Of The Jewish Right To Israel As A Homeland. This Is A Mandate That Must Be Protected.</p>
    <span class="pill pill-red">Discover More</span>
  </article>
  <article class="objective" style="left:800px;top:612px">
    <h3>Maintain Israel’s Jewish<br>Identity</h3>
    <p>While Lantern of Meridel Recognizes That Jews Are Empowered With Free Choice, Particularly In Their Beliefs And Levels Of Ritual Observance, It Also Recognizes That For Israel To Maintain Its Standing As A Jewish State It Must Institutionally Retain Its TRUE TRADITIONAL Jewish Identity.</p>
    <span class="pill pill-red">Discover More</span>
  </article>
</section>

<section class="mission">
  <div class="photo" role="img" aria-label="Black and white photo of a smiling woman giving a thumbs up"></div>
  <div class="mission-copy">
    <h2>Lantern of Meridel</h2>
    <h3>Mission Statement</h3>
    <p>Lantern of Meridel Is A Grassroots Movement That Was Established To Promote Jewish Continuity, Recognizing That In The United States, Judaism And Its Continuity Are Under Attack For A Host Of Reasons, All Of Which Lantern of Meridel Believes Must Be Identified, Understood, And Addressed In The Appropriate Manner.</p>
    <p>Lantern of Meridel Is Non-Political. We Believe That All American Jews, Regardless Of Ideological Belief, Can Embrace The Concept That In Order To Ensure The Survival Of The Jewish People There Must Be Jewish People.</p>
    <p>At The Annual Passover Seder We Say That “In Every Generation They Stand Ready To Annihilate Us.” - This Is Both Historically Accurate And Currently Relevant.</p>
  </div>
</section>

<section class="quote">
  <div class="photo" role="img" aria-label="Photo of people gathered together under a deep blue overlay"></div>
  <div class="rule"></div>
  <blockquote>“By Connecting Jews To Their Heritage, History<br>And Faith, We Can Ensure That Global Jewry Not<br>Only Survives, But Surges.”</blockquote>
</section>

<footer class="site-footer">
  <div class="footer-col"><h4 style="left:226px;top:60px">Quick Links</h4></div>
  <div class="quick-links">
    Home<br>Resist Assimilation<br>Confront Anti-Semitism<br>Expose BDS<br>Instill Jewish Pride<br>Israel: The Eternal Jewish Homeland<br>Maintain Israel’s Jewish Identity<br>New Law Increases Hate Crimes<br>Privacy Policy
  </div>
  <div class="divider" style="left:410px"></div>
  <div class="footer-col"><h4 style="left:530px;top:60px">Get In Touch</h4></div>
  <form class="contact-form">
    <div class="field">Name</div>
    <div class="field">Email</div>
    <div class="field">Phone</div>
    <div class="field">City</div>
    <div class="submit">Take Action</div>
  </form>
  <div class="divider" style="left:780px"></div>
  <div class="footer-col"><h4 style="left:838px;top:60px">Jewish Continuity</h4></div>
  <div class="about">
    Israel Is The Geographical Anchor Of Judaism, The Torah Is The Ideological/Theological Anchor Of Judaism
    <div class="socials"><span></span><span></span><span></span></div>
    <div class="copyright">Copyright © 2020 Lantern of Meridel &nbsp;|&nbsp; Privacy Policy</div>
  </div>
</footer>

</body>
</html>
```